Business card for massage therapy company called Brook Fern Wellness

Need business card for massage therapy company called Brook Fern Wellness. Would like my logo on the front and the back of the card I have 3 options of logos and you can play with what looks better.

Would like this information displayed on the back of the card:

Marcus Ellery
Licensed Massage Therapist
321-555-0147
brookfern-example.com
brookfern_rest_

```html
<!DOCTYPE html>
<html lang="en">
<head>
<meta charset="UTF-8">
<title>Brook Fern Wellness – Business Card</title>
<link rel="stylesheet" href="https://fonts.googleapis.com/css2?family=Marcellus&family=Montserrat:wght@400;500&display=swap">
<style>
  :root {
    --backdrop: #efe4d7;
    --card-front: #e8e8e8;
    --card-back: #e3e7ea;
    --sage: #6f7760;
    --clay: #c0895f;
    --ink: #3b3e43;
    --icon: #d8763a;
    --shadow: rgba(90, 70, 50, 0.18);
  }
  * { box-sizing: border-box; margin: 0; padding: 0; }
  html, body {
    width: 960px;
    height: 1200px;
    overflow: hidden;
    background: var(--backdrop);
  }
  .canvas {
    position: relative;
    width: 960px;
    height: 1200px;
  }
  .card {
    position: absolute;
    left: 100px;
    width: 760px;
    height: 434px;
    box-shadow: 0 6px 18px var(--shadow);
  }
  .card--front { top: 140px; background: var(--card-front); }
  .card--back  { top: 626px; background: var(--card-back); }

  /* Front */
  .front-brand {
    position: absolute;
    inset: 0;
    display: flex;
    align-items: center;
    justify-content: center;
    gap: 22px;
  }
  .brand-dot {
    width: 18px;
    height: 18px;
    border-radius: 50%;
    background: var(--sage);
  }
  .brand-name {
    font-family: "Marcellus", serif;
    color: var(--sage);
    font-weight: 400;
    text-align: center;
    line-height: 1.1;
  }
  .front-brand .brand-name { font-size: 60px; letter-spacing: 2px; }

  /* Back */
  .back-brand {
    position: absolute;
    left: 40px;
    top: 0;
    width: 280px;
    height: 100%;
    display: flex;
    flex-direction: column;
    align-items: center;
    justify-content: center;
    gap: 18px;
  }
  .brand-ring {
    width: 112px;
    height: 112px;
    border: 1.5px solid var(--sage);
    border-radius: 50%;
  }
  .back-brand .brand-name {
    font-size: 27px;
    letter-spacing: 3px;
    text-transform: uppercase;
  }
  .divider {
    position: absolute;
    left: 358px;
    top: 102px;
    width: 1.5px;
    height: 232px;
    background: var(--sage);
  }
  .contact-block {
    position: absolute;
    left: 398px;
    top: 112px;
  }
  .person-name {
    font-family: "Marcellus", serif;
    font-size: 31px;
    color: var(--sage);
    letter-spacing: 0.5px;
    text-transform: uppercase;
    line-height: 1;
  }
  .person-role {
    font-family: "Montserrat", sans-serif;
    font-size: 19px;
    color: var(--ink);
    margin-top: 14px;
  }
  .contact-list {
    list-style: none;
    margin-top: 40px;
    display: flex;
    flex-direction: column;
    gap: 10px;
  }
  .contact-item {
    display: flex;
    align-items: center;
    gap: 9px;
    font-family: "Montserrat", sans-serif;
    font-size: 19px;
    color: var(--ink);
  }
  .contact-icon { width: 17px; height: 17px; flex: none; }
</style>
</head>
<body>
<div class="canvas">

  <section class="card card--front">
    <div class="front-brand">
      <span class="brand-dot"></span>
      <p class="brand-name">Brook Fern<br>Wellness</p>
    </div>
  </section>

  <section class="card card--back">
    <div class="back-brand">
      <span class="brand-ring"></span>
      <p class="brand-name">Brook Fern<br>Wellness</p>
    </div>

    <span class="divider"></span>

    <div class="contact-block">
      <h1 class="person-name">Marcus Ellery</h1>
      <p class="person-role">Licensed Massage Therapist</p>
      <ul class="contact-list">
        <li class="contact-item">
          <svg class="contact-icon" viewBox="0 0 24 24" fill="none" stroke="var(--icon)" stroke-width="2" stroke-linecap="round" stroke-linejoin="round">
            <path d="M22 16.9v3a2 2 0 0 1-2.2 2 19.8 19.8 0 0 1-8.6-3.1 19.5 19.5 0 0 1-6-6A19.8 19.8 0 0 1 2.1 4.2 2 2 0 0 1 4.1 2h3a2 2 0 0 1 2 1.7c.1.9.4 1.9.7 2.8a2 2 0 0 1-.5 2.1L8 9.9a16 16 0 0 0 6 6l1.3-1.3a2 2 0 0 1 2.1-.4c.9.3 1.8.6 2.8.7a2 2 0 0 1 1.7 2z"/>
          </svg>
          321-555-0147
        </li>
        <li class="contact-item">
          <svg class="contact-icon" viewBox="0 0 24 24" fill="none" stroke="var(--icon)" stroke-width="1.8">
            <circle cx="12" cy="12" r="10"/>
            <path d="M2 12h20M12 2a15 15 0 0 1 0 20M12 2a15 15 0 0 0 0 20"/>
          </svg>
          brookfern-example.com
        </li>
        <li class="contact-item">
          <svg class="contact-icon" viewBox="0 0 24 24" fill="none" stroke="var(--icon)" stroke-width="2">
            <circle cx="12" cy="12" r="9"/>
          </svg>
          brookfern_rest_
        </li>
      </ul>
    </div>
  </section>

</div>
</body>
</html>
```